Website Design für Reinigungsunternehmen
Zielgruppe
Wir sind ein Reinigungsunternehmen, dass seit 2014 am Markt ist.
Was machen wir:
Das Angebot besteht darin, Räume nach dem IFSG (Infektionsschutzgesetz) und den Richtlinien des Werner Lasko Instituts mit ausgewählten Verfahren keimfrei zu bekommen.
Hygiene und prophylaktische Desinfektion sind für die Nutzung stark frequentierter Räume und Oberflächen gerade jetzt essentiell, denn die Ausbreitung von Viren und Bakterien kann auch durch präventive Maßnahmen eingedämmt werden.
Das Angebot ist, mit speziellen Reinigungsverfahren in Kombination mit Kaltverneblung ,die Räume fast vollständig von Keimen, Viren und Bakterien zu befreien.
So ist auch die Desinfektion von schwer zugänglichen Stellen und Gegenständen gewährleistet. Die eingesetzte Kaltnebeltechnologie wirkt in Verbindung mit Wasserstoffperoxid in verschiedenen Konzentrationen sowohl bakterizid, viruzid als auch fungizid. Wasserstoffperoxid wird rückstandsfrei abgebaut. Nach einer Einwirkzeit kann der behandelte, desinfizierte Raum sofort mechanisch gelüftet werden – ohne Material oder Umweltschäden zu riskieren.
Hier ein kurzes und erklärendes Video: https://klipvid.example/Qx7tmRwPaen
Aufgabenstellung
Die Website Soll maximal 3 Seiten haben.. Home (bzw. was wir machen..) Über uns (wer wir sind..) und Kontakt (-daten.
Ich möchte relativ kurz und knapp zum Thema kommen. Wenig Text, nur das wesentliche auf den Punkt gebracht - dafür ein ansprechendes professionelles Design. Bitte keine Bilder mit Gebäude, Reiniger etc. - dafür andere kreative Assoziationen einbringen.

```html
<!DOCTYPE html>
<html lang="de">
<head>
<meta charset="utf-8">
<title>Nivera Gebäudereinigung – Kontakt</title>
<link rel="stylesheet" href="https://fonts.googleapis.com/css2?family=Montserrat:ital,wght@0,400;0,500;0,600;0,700;1,400&display=swap">
<style>
:root{
  --navy:#1f3260;
  --ink:#1d3461;
  --brand:#1b4f96;
  --sky:#6aa8d4;
  --sky-soft:#5ba3d6;
  --water-deep:#b9d3ea;
  --water-light:#eef5fb;
  --footer:#f1f1f1;
  --white:#ffffff;
  --field:#e2e2e2;
  --rule:#d6d6d6;
}
*{margin:0;padding:0;box-sizing:border-box}
html,body{width:1200px;height:875px;overflow:hidden}
body{position:relative;background:var(--white);font-family:"Montserrat",sans-serif;color:var(--ink)}

.main-nav{position:absolute;top:25px;left:0;width:1200px;height:31px}
.main-nav a{position:absolute;top:0;height:31px;line-height:31px;font-size:11.5px;font-weight:600;color:var(--ink);text-decoration:none;letter-spacing:.2px}
.main-nav .nav-home{left:458px}
.main-nav .nav-services{left:548px}
.main-nav .nav-contact{left:663px;width:96px;text-align:center;border:1.5px solid var(--sky);border-radius:16px;color:var(--sky);font-weight:700}

.hero{position:absolute;top:0;left:0;width:1200px;height:337px}
.splash{position:absolute;top:105px;width:450px;height:170px}
.splash-left{left:0;background:linear-gradient(90deg,var(--water-deep),var(--water-light))}
.splash-right{left:750px;background:linear-gradient(270deg,var(--water-deep),var(--water-light))}

.brand{position:absolute;display:flex;align-items:center;color:var(--brand);font-weight:600}
.brand-dot{border-radius:50%;background:var(--brand)}
.hero-brand{left:499px;top:118px;gap:14px}
.hero-brand .brand-dot{width:48px;height:48px}
.hero-brand .brand-name{font-size:54px;line-height:1;letter-spacing:-.5px}
.hero-brand .brand-sub{position:absolute;left:110px;top:54px;font-size:7px;letter-spacing:2.2px;font-weight:600}

.contact-band{position:absolute;top:337px;left:0;width:1200px;height:350px;background:var(--navy)}
.contact-line{position:absolute;display:flex;align-items:center;gap:19px;color:var(--white);font-weight:700;text-decoration:none}
.contact-line .icon{width:60px;height:60px;border-radius:50%;background:var(--sky);display:flex;align-items:center;justify-content:center}
.contact-line .value{font-size:34px;letter-spacing:.2px}
.line-phone{left:404px;top:105px}
.line-mail{left:390px;top:185px}

.site-footer{position:absolute;top:687px;left:0;width:1200px;height:188px;background:var(--footer);font-size:9.3px}
.footer-brand{left:234px;top:30px;gap:5px}
.footer-brand .brand-dot{width:20px;height:20px}
.footer-brand .brand-name{font-size:22px;line-height:1}
.company{position:absolute;left:234px;top:71px;line-height:10.6px}
.company .company-name{color:var(--sky-soft);font-weight:600;font-size:8.8px}
.col-title{position:absolute;top:35px;font-size:8.8px;font-weight:700;letter-spacing:.2px}
.col-links{left:484px}
.col-contact{left:609px}
.col-news{left:797px}
.link-list{position:absolute;list-style:none}
.link-list li{height:21px;line-height:12px;display:flex;align-items:center;gap:5px}
.quick-list{left:484px;top:68px}
.contact-list{left:609px;top:68px}
.newsletter-field{position:absolute;left:797px;top:54px;width:168px;height:32px;border-radius:4px;background:var(--field);display:flex;align-items:center;justify-content:space-between;padding:0 9px 0 11px}
.newsletter-field span{font-style:italic;color:#a3a3a3;font-size:9.3px}
.newsletter-note{position:absolute;left:797px;top:97px;width:170px;font-size:7.5px;line-height:8.2px}
.footer-rule{position:absolute;left:234px;top:157px;width:732px;height:1px;background:var(--rule)}
.copyright{position:absolute;top:168px;left:0;width:1200px;text-align:center;font-size:7.6px;font-weight:500}
.copyright b{color:var(--sky-soft);font-weight:600}
</style>
</head>
<body>

<nav class="main-nav">
  <a class="nav-home" href="#">HOME</a>
  <a class="nav-services" href="#">LEISTUNGEN</a>
  <a class="nav-contact" href="#">KONTAKT</a>
</nav>

<header class="hero">
  <div class="splash splash-left" role="img" aria-label="Foto: Wasserspritzer aus klarem Wasser, von links ins Bild fließend"></div>
  <div class="splash splash-right" role="img" aria-label="Foto: Wasserspritzer aus klarem Wasser, nach rechts aus dem Bild fließend"></div>

  <div class="brand hero-brand">
    <span class="brand-dot"></span>
    <span class="brand-name">nivera</span>
    <span class="brand-sub">GEBÄUDEREINIGUNG</span>
  </div>
</header>

<section class="contact-band">
  <a class="contact-line line-phone" href="#">
    <span class="icon">
      <svg width="30" height="30" viewBox="0 0 24 24" aria-hidden="true"><path fill="#fff" d="M6.6 10.8a15.1 15.1 0 0 0 6.6 6.6l2.2-2.2a1 1 0 0 1 1-.25 11.4 11.4 0 0 0 3.6.57 1 1 0 0 1 1 1V20a1 1 0 0 1-1 1A17 17 0 0 1 3 4a1 1 0 0 1 1-1h3.5a1 1 0 0 1 1 1c0 1.25.2 2.450.57 3.57a1 1 0 0 1-.25 1z"/></svg>
    </span>
    <span class="value">09471 / 318 440 20</span>
  </a>
  <a class="contact-line line-mail" href="#">
    <span class="icon">
      <svg width="28" height="20" viewBox="0 0 28 20" aria-hidden="true"><rect x="0" y="0" width="28" height="20" rx="2" fill="#fff"/><path d="M1.5 2 L14 12 L26.5 2" fill="none" stroke="#6aa8d4" stroke-width="2.2"/></svg>
    </span>
    <span class="value">mail@nivera-group.de</span>
  </a>
</section>

<footer class="site-footer">
  <div class="brand footer-brand">
    <span class="brand-dot"></span>
    <span class="brand-name">nivera</span>
  </div>
  <div class="company">
    <div class="company-name">NIVERA GROUP</div>
    <div>Gebäudereinigung &amp; Hygienekonzepte</div>
    <div>Lindenhofweg 4</div>
    <div>93199 Kallmering</div>
  </div>

  <h4 class="col-title col-links">QUICK LINKS</h4>
  <ul class="link-list quick-list">
    <li>HOME</li>
    <li>LEISTUNGEN</li>
    <li>KONTAKT</li>
  </ul>

  <h4 class="col-title col-contact">KONTAKT UNS</h4>
  <ul class="link-list contact-list">
    <li><svg width="12" height="12" viewBox="0 0 24 24" aria-hidden="true"><path fill="#6aa8d4" d="M6.6 10.8a15.1 15.1 0 0 0 6.6 6.6l2.2-2.2a1 1 0 0 1 1-.25 11.4 11.4 0 0 0 3.6.57 1 1 0 0 1 1 1V20a1 1 0 0 1-1 1A17 17 0 0 1 3 4a1 1 0 0 1 1-1h3.5a1 1 0 0 1 1 1c0 1.25.2 2.45.57 3.57a1 1 0 0 1-.25 1z"/></svg>09471 / 318 440 20</li>
    <li><svg width="12" height="12" viewBox="0 0 12 12" aria-hidden="true"><rect x="3" y="0" width="6" height="5" fill="#6aa8d4"/><rect x="1" y="5" width="10" height="5" rx="1" fill="#6aa8d4"/><rect x="3" y="9" width="6" height="3" fill="#4f8fc0"/></svg>09471 / 318 440 29</li>
    <li><svg width="12" height="9" viewBox="0 0 28 20" aria-hidden="true"><rect width="28" height="20" rx="2" fill="#6aa8d4"/><path d="M1.5 2 L14 12 L26.5 2" fill="none" stroke="#fff" stroke-width="2.5"/></svg>mail@nivera-group.de</li>
  </ul>

  <h4 class="col-title col-news">NEWSLETTER</h4>
  <div class="newsletter-field">
    <span>Email address</span>
    <svg width="12" height="9" viewBox="0 0 28 20" aria-hidden="true"><rect width="28" height="20" rx="2" fill="#6aa8d4"/><path d="M1.5 2 L14 12 L26.5 2" fill="none" stroke="#fff" stroke-width="2.5"/></svg>
  </div>
  <p class="newsletter-note">Lorem ipsum dolor sit amet, consectetur adipiscing elit</p>

  <div class="footer-rule"></div>
  <p class="copyright">ALL RIGHTS RESERVED BY <b>NIVERA GROUP</b></p>
</footer>

</body>
</html>
```